New Car Wrap Design Project

van wrap to enhance brand awareness
Wrap is for a 2019 Varlo Midline L2H1.
my requirements are for a matt black wrap with the company logo , contact details,
www.corvalepipework.example
info@corvalepipework.example
tel:- 01632 960218
WhatsApp:- 07700900415
Facebook, instagram, YouTube & TikTok & X logos
i am very open to ideas just really want the van to be an eye catcher whilst looking elegant.

```html
<!DOCTYPE html>
<html lang="en">
<head>
<meta charset="utf-8">
<title>Corvale Pipework – Van Side Wrap</title>
<link rel="stylesheet" href="https://fonts.googleapis.com/css2?family=Montserrat:wght@500;600;700&family=Michroma&display=swap">
<style>
  :root {
    --bg: #e9e9e9;
    --wrap-black: #0b0b0c;
    --flame-orange: #e2581b;
    --flame-deep: #7a1c05;
    --ice-blue: #1a4fe0;
    --ice-deep: #0a1f7a;
    --text-white: #ffffff;
  }
  html, body { margin: 0; padding: 0; }
  body {
    width: 1200px; height: 1001px; overflow: hidden;
    background: var(--bg);
    position: relative;
    font-family: "Montserrat", sans-serif;
  }
  .wrap-panel {
    position: absolute; left: 80px; top: 320px;
    width: 1050px; height: 370px;
    border-radius: 28px; overflow: hidden;
    background: var(--wrap-black);
  }
  .wrap-art { position: absolute; inset: 0; }
  .brand-name {
    position: absolute; left: 196px; top: 100px;
    width: 220px; text-align: center;
    color: var(--text-white);
    font-weight: 600; font-size: 34px; letter-spacing: 7px;
  }
  .brand-tagline {
    position: absolute; left: 196px; top: 178px; width: 220px;
    text-align: center; color: var(--text-white);
    font-weight: 600; font-size: 8.5px; letter-spacing: 1px;
  }
  .brand-rule {
    position: absolute; left: 176px; top: 195px;
    width: 237px; height: 3px; background: #d8d8d8;
  }
  .phones {
    position: absolute; left: 426px; top: 140px;
    color: var(--text-white);
    font-family: "Michroma", sans-serif; font-size: 18px; line-height: 23px;
  }
  .phone-line { display: flex; align-items: center; gap: 6px; }
  .phone-line svg { width: 12px; height: 12px; }
  .email {
    position: absolute; left: 210px; top: 215px;
    color: var(--text-white); font-weight: 600; font-size: 12px;
  }
  .website {
    position: absolute; left: 210px; top: 233px;
    color: var(--text-white); font-weight: 700; font-size: 23.5px; letter-spacing: 0.3px;
  }
  .socials {
    position: absolute; left: 488px; top: 268px;
    display: flex; gap: 20px;
  }
  .social-dot {
    width: 18px; height: 18px; border-radius: 50%;
    border: 1.5px solid var(--text-white);
  }
</style>
</head>
<body>
  <section class="wrap-panel" aria-label="Van side wrap layout">
    <svg class="wrap-art" width="1050" height="370" viewBox="0 0 1050 370">
      <defs>
        <radialGradient id="flame-left" cx="0.05" cy="0.45" r="0.8">
          <stop offset="0" stop-color="#ff8a2a"/>
          <stop offset="0.35" stop-color="var(--flame-orange)"/>
          <stop offset="0.7" stop-color="var(--flame-deep)"/>
          <stop offset="1" stop-color="var(--wrap-black)" stop-opacity="0"/>
        </radialGradient>
        <radialGradient id="ice-right" cx="0.95" cy="0.55" r="0.8">
          <stop offset="0" stop-color="#2f6bff"/>
          <stop offset="0.4" stop-color="var(--ice-blue)"/>
          <stop offset="0.75" stop-color="var(--ice-deep)"/>
          <stop offset="1" stop-color="var(--wrap-black)" stop-opacity="0"/>
        </radialGradient>
      </defs>
      <rect x="0" y="0" width="330" height="370" fill="url(#flame-left)" role="img" aria-label="Orange fire and smoke artwork"/>
      <rect x="650" y="0" width="400" height="370" fill="url(#ice-right)" role="img" aria-label="Blue flame and smoke artwork"/>
      <line x1="0" y1="355" x2="1050" y2="355" stroke="#1c1c1e" stroke-width="2"/>
    </svg>

    <div class="brand-name">CORVALE</div>
    <div class="brand-tagline">PIPEWORK &amp; MAINTENANCE SW LTD</div>
    <div class="brand-rule"></div>

    <div class="phones">
      <div class="phone-line">
        <svg viewBox="0 0 24 24" aria-hidden="true"><path d="M6.6 10.8a15 15 0 0 0 6.6 6.6l2.2-2.2c.3-.3.7-.4 1-.2 1.1.4 2.3.6 3.6.6.6 0 1 .4 1 1V20c0 .6-.4 1-1 1A17 17 0 0 1 3 4c0-.6.4-1 1-1h3.5c.6 0 1 .4 1 1 0 1.3.2 2.5.6 3.6.1.3 0 .7-.2 1z" fill="#fff"/></svg>
        <span>01632 960218</span>
      </div>
      <div class="phone-line">
        <svg viewBox="0 0 24 24" aria-hidden="true"><circle cx="12" cy="12" r="9" fill="none" stroke="#fff" stroke-width="2"/><path d="M9 8.5c0 3.5 2.5 6.5 6.5 6.5" stroke="#fff" stroke-width="2" fill="none"/></svg>
        <span>07700 900415</span>
      </div>
    </div>

    <div class="email">info@corvalepipework.example</div>
    <div class="website">www.corvalepipework.example</div>

    <div class="socials" aria-label="Social media">
      <span class="social-dot"></span>
      <span class="social-dot"></span>
      <span class="social-dot"></span>
      <span class="social-dot"></span>
    </div>
  </section>
</body>
</html>
```